Kerno Solutions: searching for a flyer to trow in letterboxes for properties we are interested in

Hello ,

Introduction:
We are a company based in Luxembourg called "Kerno Solutions". We are specialized in buying properties on which we develop and build constructions before selling them.

Informations for the flyer:
We need a flyer to trow into the letter boxes of property owners letting them know that we are interested in buying their property, if they are interested they can give us a call.

The text for the flyer/letter is in the attachment called >>2020-03-11_KS_Text for flyer,letter there might be slight changes<<.

We need to look competent, professional and financially stable.

The flyer needs to be short and not over welling with information otherwise it will land in the trash.

We have decided that we don't want real pictures on the flyer, but shapes of any kind, blue prints, drawings are fine.

Format should be in DIN A4. We plan to print the flyer on both sides in two different languages, in other words the design will be the same on both sides only the text will be in a different language.

I also added our current logo and here is the design of the website that is under construction at the moment http://www.kernosolutions-example.lu/. The logo's color can be changed into a different blue or uni color (all white or all black).
Updates

Hi, First time user the howl thing started faster as expected. Furthermore, I need to catch my boss to discust the project with him and he is on a lot of meetings. Please give us a little bit more time. Thanks

Target Market(s)

Property owners

Requirements
Must have
• email, phone number, tax number (RCS), Tax number , matriculation and address.
see word file in attachment for information
Nice to have
• Our company logo, in one form or an other, you can be creative, the logo is in the attachment.
Should not have
• Real pictures

```html
<!DOCTYPE html>
<html lang="fr">
<head>
<meta charset="utf-8">
<title>Kerno Solutions – Flyer FR / LU</title>
<link rel="stylesheet" href="https://fonts.googleapis.com/css2?family=Bebas+Neue&family=Source+Sans+3:ital,wght@0,400;0,600;1,600;1,700&display=swap">
<style>
  :root {
    --backdrop: #939598;
    --blue: #29a3dc;
    --blue-mid: #1f7fb8;
    --blue-deep: #17659a;
    --navy: #1c5d8c;
    --ink: #333333;
    --bar: #38383a;
    --paper: #ffffff;
    --paper-shade: #eceef0;
  }
  * { box-sizing: border-box; margin: 0; padding: 0; }
  html, body { width: 1200px; height: 842px; overflow: hidden; }
  body { background: var(--backdrop); position: relative; font-family: "Source Sans 3", sans-serif; }

  .flyer {
    position: absolute; top: 68px; width: 596px; height: 843px;
    transform: scale(0.822); transform-origin: top left;
    background: var(--paper); overflow: hidden;
    box-shadow: 2px 3px 8px rgba(0,0,0,.35);
  }
  .flyer--fr { left: 79px; }
  .flyer--lu { left: 629px; }
  .flyer__shapes { position: absolute; inset: 0; }

  .headline {
    position: absolute; right: 24px; top: 28px;
    font-family: "Bebas Neue", sans-serif; font-size: 36px; color: var(--paper); letter-spacing: .5px;
  }
  .headline-rule { position: absolute; right: 24px; top: 82px; width: 132px; height: 2px; background: var(--paper); }
  .intro {
    position: absolute; right: 24px; top: 97px; width: 290px;
    text-align: right; color: var(--paper); font-size: 13.5px; line-height: 18px;
  }
  .intro p + p { margin-top: 18px; }

  .letter { position: absolute; left: 23px; top: 346px; width: 340px; color: var(--ink); font-size: 13.5px; line-height: 16px; }
  .letter p + p { margin-top: 16px; }
  .letter .greeting { margin-top: 32px; }
  .letter .signature { margin-top: 12px; font-weight: 700; font-style: italic; text-transform: uppercase; }

  .cta {
    position: absolute; left: 381px; top: 377px; width: 98px; height: 98px; border-radius: 50%;
    background: var(--blue); border: 3px solid var(--paper);
    box-shadow: 0 2px 6px rgba(0,0,0,.3);
    display: flex; align-items: center; justify-content: center; text-align: center;
    font-family: "Bebas Neue", sans-serif; font-size: 18px; line-height: 17px; color: var(--paper);
  }

  .brand { position: absolute; left: 31px; top: 666px; display: flex; align-items: center; gap: 8px; }
  .brand__mark { width: 16px; height: 16px; background: var(--navy); }
  .brand__name { font-family: "Bebas Neue", sans-serif; font-size: 30px; color: var(--navy); letter-spacing: .5px; }

  .contacts { position: absolute; left: 28px; top: 712px; list-style: none; font-size: 12.5px; color: var(--ink); }
  .contacts li { display: flex; align-items: center; gap: 10px; height: 19.5px; }
  .contacts svg { width: 14px; height: 14px; flex: none; }
</style>
</head>
<body>

<!-- French side -->
<article class="flyer flyer--fr" lang="fr">
  <svg class="flyer__shapes" viewBox="0 0 596 843" aria-hidden="false">
    <defs>
      <linearGradient id="houseTop" x1="0" y1="0" x2="1" y2="1">
        <stop offset="0" stop-color="#b9b6ae"/><stop offset=".5" stop-color="#8c8577"/><stop offset="1" stop-color="#5c5a4c"/>
      </linearGradient>
      <linearGradient id="houseBottom" x1="0" y1="0" x2="0" y2="1">
        <stop offset="0" stop-color="#8da3c0"/><stop offset=".5" stop-color="#c99a55"/><stop offset="1" stop-color="#4a4034"/>
      </linearGradient>
      <linearGradient id="middleTone" x1="0" y1="0" x2="0" y2="1">
        <stop offset="0" stop-color="#e4e6e8"/><stop offset=".15" stop-color="#fafafa"/><stop offset=".9" stop-color="#f4f5f6"/><stop offset="1" stop-color="#e2e4e6"/>
      </linearGradient>
      <linearGradient id="blueWash" x1="0" y1="0" x2="1" y2="1">
        <stop offset="0" stop-color="#2aa6df"/><stop offset=".6" stop-color="#1f7fb8"/><stop offset="1" stop-color="#17659a"/>
      </linearGradient>
    </defs>
    <rect x="0" y="0" width="596" height="281" fill="url(#houseTop)" role="img" aria-label="Photo d'une maison moderne avec jardin"/>
    <rect x="0" y="281" width="596" height="281" fill="url(#middleTone)"/>
    <polygon points="320,562 596,562 596,843 385,843 285,700" fill="url(#houseBottom)" role="img" aria-label="Photo d'une villa moderne éclairée au crépuscule"/>
    <polygon points="172,0 596,0 596,700 505,562 340,281 290,281" fill="url(#blueWash)" opacity=".93"/>
    <polygon points="285,200 370,200 596,640 596,843 575,843" fill="var(--blue-deep)" opacity=".55"/>
    <polygon points="315,843 382,780 400,843" fill="var(--blue-deep)"/>
    <rect x="0" y="818" width="330" height="25" fill="var(--bar)"/>
  </svg>

  <h1 class="headline">Madame, Monsieur,</h1>
  <div class="headline-rule"></div>
  <div class="intro">
    <p>Ce courrier vous a été adressé, car votre propriété a attiré notre attention.</p>
    <p>Nous souhaiterions discuter avec vous de son éventuel rachat par notre société.</p>
  </div>

  <div class="letter">
    <p>En cas d’accord, nous vous assurons une décision rapide, un paiement garanti, et zéro frais d’intermédiaire.</p>
    <p>En attendant de vos nouvelles, nous restons à votre entière disposition pour tout renseignement.</p>
    <p class="greeting">Salutations distinguées</p>
    <p class="signature">L’équipe de Kerno Solutions</p>
  </div>

  <div class="cta">Call us<br>for a<br>free quote</div>

  <div class="brand"><span class="brand__mark"></span><span class="brand__name">Kerno Solutions</span></div>
  <ul class="contacts">
    <li><svg viewBox="0 0 14 14"><rect width="14" height="14" rx="2" fill="var(--navy)"/><path d="M4 3.5l1.5-.5 1 2-1 .8a5 5 0 0 0 2.7 2.7l.8-1 2 1-.5 1.5C7.5 10.5 3.5 6.5 4 3.5z" fill="#fff"/></svg>+352 691.000.111 | 352 200.000.00</li>
    <li><svg viewBox="0 0 14 14"><rect width="14" height="14" rx="2" fill="var(--navy)"/><rect x="3" y="4" width="8" height="6" fill="none" stroke="#fff"/><path d="M3 4l4 3.2L11 4" fill="none" stroke="#fff"/></svg>kernosolutions-example.lu</li>
    <li><svg viewBox="0 0 14 14"><rect width="14" height="14" rx="2" fill="var(--navy)"/><path d="M7 2.5a3 3 0 0 1 3 3c0 2.2-3 6-3 6s-3-3.8-3-6a3 3 0 0 1 3-3z" fill="#fff"/><circle cx="7" cy="5.5" r="1.1" fill="var(--navy)"/></svg>12 rue des Prés, L-3200 Testange</li>
    <li><svg viewBox="0 0 14 14"><circle cx="7" cy="7" r="7" fill="var(--navy)"/><circle cx="7" cy="7" r="4" fill="none" stroke="#fff"/><path d="M3 7h8M7 3c-2 2.5-2 5.5 0 8M7 3c2 2.5 2 5.5 0 8" fill="none" stroke="#fff" stroke-width=".8"/></svg>info@kernosolutions-example.lu</li>
  </ul>
</article>

<!-- Luxembourgish side -->
<article class="flyer flyer--lu" lang="lb">
  <svg class="flyer__shapes" viewBox="0 0 596 843">
    <rect x="0" y="0" width="596" height="281" fill="url(#houseTop)" role="img" aria-label="Foto vun engem modernen Haus mat Gaart"/>
    <rect x="0" y="281" width="596" height="281" fill="url(#middleTone)"/>
    <polygon points="320,562 596,562 596,843 385,843 285,700" fill="url(#houseBottom)" role="img" aria-label="Foto vun enger moderner Villa am Owendliicht"/>
    <polygon points="172,0 596,0 596,700 505,562 340,281 290,281" fill="url(#blueWash)" opacity=".93"/>
    <polygon points="285,200 370,200 596,640 596,843 575,843" fill="var(--blue-deep)" opacity=".55"/>
    <polygon points="315,843 382,780 400,843" fill="var(--blue-deep)"/>
    <rect x="0" y="818" width="330" height="25" fill="var(--bar)"/>
  </svg>

  <h1 class="headline">Madame, Monsieur,</h1>
  <div class="headline-rule"></div>
  <div class="intro">
    <p>Dir kritt dëst Schreiwes well Är Proprietéit eis Opmierksamkeet zeréckbehalen huet.</p>
    <p>Mir géinge gär mat lech iwwert d’Méiglechkeet, datt eise Betrib se opkeeft, diskutéieren.</p>
  </div>

  <div class="letter">
    <p>Mir versécheren lech e séieren Entscheedungsprozess, garantéieren d’Bezuelung a verrechne keng Drëttkäschten.</p>
    <p>Mir géingen eis freeën, vun lech ze héieren, a sti ganz zu Ärer Verfügung fir zousätzlech Informatiounen.</p>
    <p class="greeting">Mat beschte Gréiss,</p>
    <p class="signature" style="margin-top:6px">D’Equipe vun Kerno Solutions</p>
  </div>

  <div class="cta">Call us<br>for a<br>free quote</div>

  <div class="brand"><span class="brand__mark"></span><span class="brand__name">Kerno Solutions</span></div>
  <ul class="contacts">
    <li><svg viewBox="0 0 14 14"><rect width="14" height="14" rx="2" fill="var(--navy)"/><path d="M4 3.5l1.5-.5 1 2-1 .8a5 5 0 0 0 2.7 2.7l.8-1 2 1-.5 1.5C7.5 10.5 3.5 6.5 4 3.5z" fill="#fff"/></svg>+352 691.000.111 | 352 200.000.00</li>
    <li><svg viewBox="0 0 14 14"><rect width="14" height="14" rx="2" fill="var(--navy)"/><rect x="3" y="4" width="8" height="6" fill="none" stroke="#fff"/><path d="M3 4l4 3.2L11 4" fill="none" stroke="#fff"/></svg>kernosolutions-example.lu</li>
    <li><svg viewBox="0 0 14 14"><rect width="14" height="14" rx="2" fill="var(--navy)"/><path d="M7 2.5a3 3 0 0 1 3 3c0 2.2-3 6-3 6s-3-3.8-3-6a3 3 0 0 1 3-3z" fill="#fff"/><circle cx="7" cy="5.5" r="1.1" fill="var(--navy)"/></svg>12 rue des Prés, L-3200 Testange</li>
    <li><svg viewBox="0 0 14 14"><circle cx="7" cy="7" r="7" fill="var(--navy)"/><circle cx="7" cy="7" r="4" fill="none" stroke="#fff"/><path d="M3 7h8M7 3c-2 2.5-2 5.5 0 8M7 3c2 2.5 2 5.5 0 8" fill="none" stroke="#fff" stroke-width=".8"/></svg>info@kernosolutions-example.lu</li>
  </ul>
</article>

</body>
</html>
```